Environmental Plastics Infographic

We need a series of infographics that can be used individually or as a combined presentation. We'd like the combined piece to include an introduction and conclusion along with 4-5 infographics. Each infographic (information unit) should also work as a standalone. We are trying to help people visualize size proportions and ratios to put carbon footprint/life cycle data for EPS foam packaging in perspective. We are looking for something creative to help people understand what the figures represent in terms they are familiar with.
To view our typical company design/style please see our website at www.corvalpackfed.org. Our primary RGB colors are: (187,140,9); (94,47,29); (94,138,164); and (164,167,15). Secondary RGB colors are (249,162,28) and (218,210,208). Our title/header font is DIN Next LT Pro and our copy font is Calibri 10.5 pt. We can deviate from the font specification if beneficial and welcome interesting text treatments and typography.
We want sufficient white space with easy to grasp message concept with visual components. The attachment showing data points present concepts on how to show the data impacts but are only representative of a baseline concept - we are confident a professional designer can do a much better job with better visual presentation.
Target Market(s)
The audience is international brand manufacturers (brindlecove, talvo), US legislators & government agencies.
Nice to have
- Other creative ideas on how to present this messaging is encouraged.

```html
<!DOCTYPE html>
<html lang="en">
<head>
<meta charset="utf-8">
<title>EPS Life Cycle Infographic Series</title>
<link href="https://fonts.googleapis.com/css2?family=Montserrat:wght@700;800&family=Open+Sans:wght@300;400;600;700&display=swap" rel="stylesheet">
<style>
:root{
  --backdrop:#7f8695;
  --olive:#a4a70f;
  --olive-soft:#c3c56a;
  --gold:#bb8c09;
  --gold-text:#b48a2c;
  --brown:#5e2f1d;
  --blue:#5e8aa4;
  --blue-pale:#a8bfd2;
  --blue-deep:#4f7d9a;
  --orange:#f9a21c;
  --stone:#dad2d0;
  --ink:#2b2b2b;
  --grey:#6f6f6f;
  --white:#ffffff;
  --yellow:#f6e11a;
}
*{margin:0;padding:0;box-sizing:border-box}
html,body{width:1000px;height:1200px;overflow:hidden}
body{background:var(--backdrop);font-family:"Open Sans",Arial,sans-serif;color:var(--ink);position:relative}
.sheet-number{position:absolute;font:300 36px/1 "Open Sans",Arial,sans-serif;color:var(--white)}
.card{position:absolute;width:446px;height:343px;background:var(--white);overflow:hidden;box-shadow:0 22px 18px -14px rgba(40,44,55,.45)}
.abs{position:absolute;z-index:2}
.band{position:absolute;z-index:0}
.ph{position:absolute;z-index:1}
.brand{position:absolute;z-index:2;display:flex;align-items:center;gap:5px}
.brand .dot{width:34px;height:34px;border-radius:50%;background:var(--gold)}
.brand .name{font:400 8px/1.1 "Open Sans",Arial,sans-serif;color:var(--gold-text);width:62px}
.brand.large .dot{width:48px;height:48px}
.brand.large .name{font-size:10px;width:74px}
.header{position:absolute;left:0;top:0;width:100%;height:83px}
.header h2{position:absolute;font:300 23px/1.25 "Open Sans",Arial,sans-serif;color:var(--white)}
.header h2 b{font:800 23px/1.25 Montserrat,Arial,sans-serif}
.corner{position:absolute;right:0;bottom:0;z-index:0}
.blue-t{color:var(--blue);font-weight:600}
.c{text-align:center}
.r{text-align:right}
</style>
</head>
<body>

<div class="sheet-number" style="left:8px;top:150px">1.</div>
<div class="sheet-number" style="left:498px;top:150px">2.</div>
<div class="sheet-number" style="left:8px;top:585px">3.</div>
<div class="sheet-number" style="left:498px;top:585px">4.</div>
<div class="sheet-number" style="left:8px;top:1018px">5.</div>
<div class="sheet-number" style="left:498px;top:1018px">6.</div>

<!-- Card 1: Global warming -->
<section class="card card-warming" style="left:44px;top:26px">
  <h2 class="abs" style="left:47px;top:18px;font:300 23px/1.15 'Open Sans',Arial,sans-serif;color:var(--olive)">EPS Life Cycle –<br><b style="font:800 23px/1.2 Montserrat,Arial,sans-serif">Global Warming</b></h2>
  <div class="brand" style="left:326px;top:30px"><span class="dot"></span><span class="name">Corval Pack Federation</span></div>

  <div class="band" style="left:0;top:83px;width:446px;height:123px;background:var(--olive)"></div>
  <div class="ph" role="img" aria-label="Silhouette of factory chimneys and city buildings" style="left:262px;top:118px;width:184px;height:88px;background:linear-gradient(180deg,#cfd18e,#c3c56a)"></div>
  <p class="abs" style="left:32px;top:114px;width:232px;font:400 15.5px/1.45 'Open Sans',Arial,sans-serif;color:var(--ink)">EPS has a very <b>low global warming impact</b> compared to other packaging materials.</p>

  <div class="band" style="left:0;top:206px;width:446px;height:24px;background:var(--gold)"></div>
  <svg class="abs" style="left:0;top:206px" width="446" height="24" aria-hidden="true">
    <g fill="#d7b96a"><polygon points="24,6 36,6 36,2 46,12 36,22 36,18 24,18"/><polygon points="158,6 170,6 170,2 180,12 170,22 170,18 158,18"/><polygon points="335,6 347,6 347,2 357,12 347,22 347,18 335,18"/></g>
  </svg>
  <span class="abs" style="left:55px;top:210px;font:700 10px 'Open Sans',Arial,sans-serif;color:var(--white)">1KM</span>
  <span class="abs" style="left:183px;top:214px;font:700 8px 'Open Sans',Arial,sans-serif;color:var(--white)">31 MILES.</span>
  <span class="abs" style="left:240px;top:210px;font:700 10px 'Open Sans',Arial,sans-serif;color:var(--white)">50km</span>
  <span class="abs" style="left:374px;top:211px;font:700 10px 'Open Sans',Arial,sans-serif;color:var(--white)">100km</span>
  <div class="ph" role="img" aria-label="Small car driving along the road" style="left:284px;top:206px;width:42px;height:20px;border-radius:10px;background:linear-gradient(90deg,#e9eef2,#8fb0c7)"></div>

  <div class="ph" role="img" aria-label="Stack of white EPS foam packaging pieces" style="left:94px;top:234px;width:126px;height:64px;background:linear-gradient(160deg,#f4f4f4,#bdbdbd)"></div>
  <svg class="abs" style="left:0;top:230px" width="446" height="50" aria-hidden="true">
    <g stroke="var(--gold)" stroke-width="2" fill="#fff">
      <line x1="64" y1="0" x2="64" y2="22"/><circle cx="64" cy="6" r="4"/>
      <line x1="194" y1="0" x2="194" y2="16"/><circle cx="194" cy="21" r="5"/>
      <line x1="252" y1="0" x2="252" y2="22"/><circle cx="252" cy="6" r="4"/>
      <line x1="389" y1="0" x2="389" y2="22"/><circle cx="389" cy="6" r="4"/>
    </g>
  </svg>
  <p class="abs c" style="left:34px;top:256px;width:60px;font:400 9.5px/1.3 'Open Sans',Arial,sans-serif;color:#9aa3ad">115.5kg<br>CO²</p>
  <p class="abs" style="left:243px;top:258px;font:700 11px 'Open Sans',Arial,sans-serif;color:var(--gold-text)">5,775kg CO²</p>
  <p class="abs" style="left:362px;top:258px;font:400 9px 'Open Sans',Arial,sans-serif;color:#9aa3ad">11,550kg CO²</p>

  <p class="abs" style="left:118px;top:301px;font:400 9.5px/1.3 'Open Sans',Arial,sans-serif;color:var(--grey)">1 TON OF EPS<br><b style="font-size:11.5px;color:var(--gold-text)">5,360kg CO²</b></p>
  <p class="abs" style="left:200px;top:302px;width:240px;font:400 7.5px/1.6 'Open Sans',Arial,sans-serif;color:var(--ink)">The carbon footprint for manufacturing <b>1 Ton of EPS</b><br>is the equivalent of driving your car <b>31 MILES.</b></p>
</section>

<!-- Card 2: Energy use -->
<section class="card card-energy" style="left:536px;top:26px">
  <div class="header" style="background:var(--olive)">
    <h2 style="left:44px;top:20px">Life Cycle – <b>Non-Renewable<br>Energy Use</b></h2>
    <svg class="abs" style="left:376px;top:22px" width="30" height="44" aria-hidden="true"><polygon points="16,2 4,24 14,24 10,42 26,16 16,16 22,2" fill="none" stroke="#fff" stroke-width="2.5" stroke-linejoin="round"/></svg>
  </div>
  <p class="abs c" style="left:22px;top:118px;width:104px;font:400 9px/1.55 'Open Sans',Arial,sans-serif"><b>EPS energy consumption</b> for the manufacture of <b>1 TON</b> of packaging material is equivalent to <b>300 HOURS</b> of light for a single lightbulb.</p>
  <div class="ph" role="img" aria-label="Glowing yellow lightbulb with radiating rays" style="left:146px;top:94px;width:124px;height:156px;border-radius:50% 50% 45% 45%;background:radial-gradient(circle at 50% 55%,var(--yellow) 0 40%,#fdf6b0 62%,#fff 72%)"></div>
  <p class="abs c" style="left:148px;top:164px;width:120px;font:700 26px/1 'Open Sans',Arial,sans-serif;color:var(--gold-text)">100<br><span style="font:300 18px 'Open Sans',Arial,sans-serif">WATT</span></p>
  <p class="abs c" style="left:100px;top:262px;width:220px;font:400 14.5px/1.4 'Open Sans',Arial,sans-serif">One 100 watt<br>lightbulb = 360 MJ</p>
  <div class="ph" role="img" aria-label="White EPS foam packaging insert" style="left:312px;top:110px;width:120px;height:100px;background:linear-gradient(160deg,#f6f6f6,#c2c2c2)"></div>
  <p class="abs c" style="left:310px;top:224px;width:130px;font:400 12.5px/1.3 'Open Sans',Arial,sans-serif">1 TON OF EPS<br><b style="font-size:15px;color:var(--blue)">108,000 MJ</b></p>
  <div class="brand" style="left:30px;top:291px"><span class="dot"></span><span class="name">Corval Pack Federation</span></div>
  <svg class="corner" width="76" height="70" aria-hidden="true"><polygon points="76,0 76,70 0,70" fill="var(--olive)"/></svg>
</section>

<!-- Card 3: Water, swimming pools -->
<section class="card card-water-pool" style="left:44px;top:414px">
  <div class="header" style="background:var(--blue)"><h2 style="left:36px;top:28px">Life Cycle – <b>Water Consumption</b></h2></div>
  <div class="ph" role="img" aria-label="Blue swimming pool with ladder" style="left:0;top:168px;width:200px;height:136px;clip-path:polygon(0 0,100% 4%,100% 30%,0 98%);background:linear-gradient(180deg,#5e8fb6,#8ab8d8)"></div>
  <div class="ph" role="img" aria-label="Water droplet" style="left:46px;top:108px;width:32px;height:48px;border-radius:50% 50% 50% 50%/65% 65% 40% 40%;background:linear-gradient(160deg,#fff,#9fd0ec)"></div>
  <p class="abs" style="left:88px;top:108px;font:400 10.5px/1.45 'Open Sans',Arial,sans-serif"><b style="font-size:12.5px">24,000 gallons</b><br>One 40x20 foot<br>swimming pool<br><i style="font-size:7px;padding-left:26px">(avg 4 ft depth)</i></p>
  <p class="abs r" style="left:200px;top:103px;width:195px;font:400 12px/1.4 'Open Sans',Arial,sans-serif;color:var(--grey)">The amount of water used to manufacture <span class="blue-t">1,000 EPS shipping</span> containers is the equivalent of <span class="blue-t">xx</span> swimming pools.</p>
  <div class="ph" role="img" aria-label="White EPS shipping cooler box" style="left:314px;top:178px;width:104px;height:92px;background:linear-gradient(160deg,#fafafa,#c9c9c9)"></div>
  <p class="abs r" style="left:190px;top:208px;width:116px;font:400 11px/1.45 'Open Sans',Arial,sans-serif"><span class="blue-t" style="font-size:12px">1 TON OF EPS</span><br>foam uses <span class="blue-t">xxx gallons</span> water to manufacture.</p>
  <p class="abs" style="left:238px;top:279px;font:400 7.5px/1.5 'Open Sans',Arial,sans-serif;color:#9a9a9a">A typical EPS shipping container<br>15x13x12 inches weighs 2 lbs.</p>
  <div class="brand" style="left:30px;top:291px"><span class="dot"></span><span class="name">Corval Pack Federation</span></div>
  <svg class="corner" width="76" height="70" aria-hidden="true"><polygon points="76,0 76,70 0,70" fill="var(--blue)"/></svg>
</section>

<!-- Card 4: Water, corrugated comparison -->
<section class="card card-water-paper" style="left:536px;top:414px">
  <div class="header" style="background:var(--blue)"><h2 style="left:40px;top:28px">Life Cycle - <b>Water Consumption</b></h2></div>
  <div class="ph" role="img" aria-label="Water droplet behind a stack of white EPS containers" style="left:48px;top:104px;width:84px;height:112px;background:linear-gradient(170deg,#d4ecf7,#f1f1f1 60%,#cfcfcf)"></div>
  <p class="abs" style="left:32px;top:226px;font:400 10.5px/1.45 'Open Sans',Arial,sans-serif"><span class="blue-t" style="font-size:13px">1 TON of EPS</span><br>uses <b>xxx gallons</b> water<br>to manufacture.</p>
  <p class="abs c" style="left:156px;top:110px;width:172px;font:400 11.5px/1.45 'Open Sans',Arial,sans-serif">The amount of water used to manufacture <span class="blue-t">1,000 EPS</span> shipping containers is a <span class="blue-t">miniscule amount</span> compared to corrugated paper.</p>
  <div class="ph" role="img" aria-label="Large water droplet behind an open cardboard box" style="left:334px;top:92px;width:96px;height:144px;background:linear-gradient(170deg,#cfe9f6,#e6eff4 45%,#b98a5a 60%,#8a6238)"></div>
  <p class="abs r" style="left:270px;top:242px;width:158px;font:400 9.5px/1.45 'Open Sans',Arial,sans-serif"><span class="blue-t" style="font-size:11px">1 TON Corrugated Paper.</span><br>uses <b>xxx gallons</b> water<br>to manufacture.</p>
  <div class="brand" style="left:30px;top:291px"><span class="dot"></span><span class="name">Corval Pack Federation</span></div>
  <svg class="corner" width="76" height="70" aria-hidden="true"><polygon points="76,0 76,70 0,70" fill="var(--blue)"/></svg>
</section>

<!-- Card 5: Landfill diversion -->
<section class="card card-recycling" style="left:44px;top:810px">
  <div class="brand large" style="left:312px;top:20px"><span class="dot"></span><span class="name">Corval Pack Federation</span></div>
  <div class="band" style="left:0;top:83px;width:446px;height:143px;background:var(--orange)"></div>
  <svg class="abs" style="left:80px;top:92px" width="90" height="86" aria-hidden="true">
    <path d="M38 12 a7 7 0 0 1 14 0" fill="none" stroke="var(--blue)" stroke-width="4"/>
    <polygon points="16,14 74,14 84,84 6,84" fill="var(--blue)"/>
  </svg>
  <p class="abs c" style="left:80px;top:126px;width:90px;font:700 20px/1 'Open Sans',Arial,sans-serif;color:var(--white);letter-spacing:-.5px">19,850<br><span style="font-size:11px">TONS</span></p>
  <p class="abs c" style="left:50px;top:183px;width:150px;font:400 13px/1.35 'Open Sans',Arial,sans-serif"><b>EPS diverted</b> from<br>the landfill in <b>2018</b></p>
  <span class="abs" style="left:210px;top:122px;font:400 34px 'Open Sans',Arial,sans-serif;color:var(--white)">=</span>
  <div class="ph" role="img" aria-label="Figure throwing rubbish into a bin" style="left:284px;top:98px;width:64px;height:56px;background:linear-gradient(90deg,#6a2e12,#4a2010)"></div>
  <p class="abs c" style="left:222px;top:159px;width:210px;font:400 14px/1.38 'Open Sans',Arial,sans-serif">The equivalent of waste generated by <b>13,233</b> U.S. households</p>
  <p class="abs" style="left:44px;top:254px;font:400 11px 'Open Sans',Arial,sans-serif">This EPS was used to make:</p>
  <div class="ph" role="img" aria-label="Picture frame icon" style="left:38px;top:275px;width:34px;height:32px;background:#2b2b2b"></div>
  <div class="ph" role="img" aria-label="Surfboard icon" style="left:100px;top:273px;width:30px;height:34px;background:#d0d0d0"></div>
  <div class="ph" role="img" aria-label="Coat hanger icon" style="left:148px;top:276px;width:48px;height:30px;background:#3a3a3a"></div>
  <span class="abs" style="left:210px;top:276px;font:400 12px 'Open Sans',Arial,sans-serif">AND</span>
  <div class="ph" role="img" aria-label="Recycled EPS packaging tray outline" style="left:260px;top:268px;width:60px;height:42px;background:#e2e2e2"></div>
  <p class="abs" style="left:323px;top:271px;font:400 7.5px/1.3 'Open Sans',Arial,sans-serif">Recycled<br>content EPS<br>packaging</p>
  <div class="ph" role="img" aria-label="Polystyrene recycling code 6" style="left:372px;top:278px;width:34px;height:34px;background:#e9e9e9"></div>
  <svg class="corner" width="76" height="70" aria-hidden="true"><polygon points="76,0 76,70 0,70" fill="var(--blue)"/></svg>
</section>

<!-- Card 6: Total CO2 comparison -->
<section class="card card-impact" style="left:536px;top:810px;background:var(--blue-pale)">
  <svg class="band" style="left:0;top:0" width="446" height="343" aria-hidden="true">
    <polygon points="257,0 446,0 446,343 198,343" fill="var(--olive)"/>
    <polygon points="226,290 344,290 318,343 200,343" fill="#fff"/>
  </svg>
  <p class="abs" style="left:57px;top:18px;font:700 13.5px/1.4 'Open Sans',Arial,sans-serif">EPS U.S.<br>manufacturing<br>in 2017 was</p>
  <p class="abs" style="left:56px;top:74px;font:800 27px/1 Montserrat,Arial,sans-serif;color:var(--white)">6.35</p>
  <p class="abs" style="left:56px;top:104px;font:700 11.5px 'Open Sans',Arial,sans-serif;color:var(--white)">MILLION TONS</p>
  <div class="ph" role="img" aria-label="Large white EPS foam packaging pieces" style="left:100px;top:120px;width:150px;height:134px;background:linear-gradient(150deg,#ffffff,#d6dde3 70%,#b7c4cf)"></div>
  <div class="abs" style="left:16px;top:136px;width:100px;height:48px;border:1px solid var(--ink);border-left:none;background:var(--blue-pale)"></div>
  <p class="abs" style="left:27px;top:140px;width:88px;font:400 9px/1.5 'Open Sans',Arial,sans-serif"><b>Each ton</b> of EPS production emits <b>.5360 kg/tn CO²</b></p>
  <div class="ph" role="img" aria-label="Puffs of white smoke" style="left:16px;top:246px;width:34px;height:66px;border-radius:17px;background:linear-gradient(180deg,#fff,#e2e9ef)"></div>
  <p class="abs" style="left:60px;top:241px;font:400 10px 'Open Sans',Arial,sans-serif">Total CO² Impact</p>
  <div class="abs c" style="left:56px;top:256px;width:86px;height:40px;border-radius:20px;background:var(--blue-deep);font:800 31px/40px Montserrat,Arial,sans-serif;color:var(--white)">3.5</div>
  <p class="abs" style="left:60px;top:304px;font:700 11.5px 'Open Sans',Arial,sans-serif">MILLION TONS</p>

  <div class="ph" role="img" aria-label="Six small cars seen from above" style="left:262px;top:36px;width:54px;height:70px;background:repeating-linear-gradient(90deg,#e8eef2 0 14px,transparent 14px 20px)"></div>
  <p class="abs" style="left:330px;top:38px;font:800 21px/1 Montserrat,Arial,sans-serif;color:var(--white)">272.48</p>
  <p class="abs" style="left:330px;top:62px;font:700 12px/1.4 'Open Sans',Arial,sans-serif">million cars<br>registered in<br>the U.S. in 2017</p>
  <div class="abs" style="left:255px;top:130px;width:160px;height:38px;border:1px solid var(--ink)"></div>
  <p class="abs" style="left:268px;top:134px;font:400 9.5px/1.45 'Open Sans',Arial,sans-serif">Each car emits an average<br>of <b>7 tns of CO²/year</b></p>
  <div class="ph" role="img" aria-label="Car from above with exhaust smoke" style="left:244px;top:186px;width:28px;height:96px;border-radius:14px;background:linear-gradient(180deg,#f2f5f7 0 60%,#dbe3e8)"></div>
  <p class="abs" style="left:296px;top:186px;font:400 13.5px 'Open Sans',Arial,sans-serif">Total CO² Impact</p>
  <div class="abs c" style="left:292px;top:206px;width:110px;height:40px;border:2px solid var(--white);border-radius:20px;font:800 31px/36px Montserrat,Arial,sans-serif;color:var(--white)">1.907</div>
  <p class="abs" style="left:295px;top:253px;font:700 15.5px 'Open Sans',Arial,sans-serif">BILLION TONS</p>
  <div class="brand" style="left:226px;top:300px"><span class="dot"></span><span class="name">Corval Pack Federation</span></div>
</section>

</body>
</html>
```